UI/UX Design for AI Photo-to-Video Web Platform (Figma)

I am looking for a modern, high-converting redesign for my Next.js-based web platform. The service allows users to transform old photos into vibrant memories using AI. The design needs to be clean, intuitive, and "mobile-ready" (responsive).
Key Features to Visualize on the Homepage:
Photo Restoration & Colorization: A clear "before/after" visual showing a black-and-white photo turning into a high-quality color photo.
Photo-to-Video Animation: A visual representation of how both B&W and color photos are transformed into dynamic video clips.
Story Creation: A section showing how these photos and videos are combined into a single "Story Video" with background music.
Scope of Work:
Homepage Redesign: A hero section with the core value proposition and a visual walkthrough of the process.
Service/Internal Pages: Redesigning the functional pages where users upload files and manage their projects.
Responsive Design: While the focus is desktop, the layout must be designed with a "Mobile-First" mindset for easy porting to a mobile app later.
Technical Requirements for the Designer:
Tool: Must be designed in Figma.
Structure: Use Figma Auto Layout and Components for all elements (buttons, inputs, cards).
Design System: Provide a clear style guide (Typography, Color Palette, Spacing).
Assets: All icons should be in SVG format.
Style Preference:
Modern, sleek, and trustworthy.
Since the product is about "memories," the vibe should be emotional yet technologically advanced (AI-driven).

```html
<!DOCTYPE html>
<html lang="en">
<head>
<meta charset="UTF-8">
<title>huevista.ai – Upload Images</title>
<link href="https://fonts.googleapis.com/css2?family=Poppins:wght@400;500;600;700&display=swap" rel="stylesheet">
<style>
  :root {
    --bg: #f5f4f1;
    --surface: #ffffff;
    --ink: #0f1b34;
    --ink-soft: #2b2f38;
    --muted: #6b6f78;
    --accent: #f5a524;
    --danger: #e0383e;
    --tile-empty: #f1f1ef;
    --dash: #4a5266;
    --done: #36b24a;
  }
  * { box-sizing: border-box; margin: 0; padding: 0; }
  html, body {
    width: 1200px; height: 3498px; overflow: hidden;
    background: var(--bg);
    font-family: "Poppins", sans-serif;
    color: var(--ink);
  }
  .screen {
    position: relative;
    width: 400px; height: 1166px;
    transform: scale(3); transform-origin: 0 0;
  }
  .abs { position: absolute; }

  /* Header */
  .brand { left: 22px; top: 20px; font-size: 23px; font-weight: 700; letter-spacing: -0.2px; }
  .meter { top: 22px; font-size: 13px; line-height: 15px; font-weight: 500; }
  .meter .top { color: var(--ink); }
  .meter .bottom { color: var(--accent); }
  .avatar {
    left: 341px; top: 18px; width: 39px; height: 39px; border-radius: 50%;
    background: var(--accent); color: var(--ink);
    display: flex; align-items: center; justify-content: center;
    font-weight: 600; font-size: 16px;
  }

  /* Tabs */
  .tabs {
    left: 22px; top: 75px; width: 358px; height: 57px;
    background: var(--surface); border-radius: 10px;
  }
  .tab { top: 20px; font-size: 14px; font-weight: 500; color: var(--ink); }
  .tab-indicator { left: 17px; top: 54px; width: 96px; height: 3px; background: var(--accent); border-radius: 2px; }

  /* Section headings */
  .section-title { left: 22px; font-size: 20px; font-weight: 700; }
  .section-copy { left: 22px; width: 360px; font-size: 15px; line-height: 23px; color: var(--ink-soft); }

  /* Upload */
  .upload {
    left: 22px; top: 258px; width: 358px; height: 288px;
    background: var(--surface); border-radius: 20px;
  }
  .dropzone {
    position: absolute; left: 7px; top: 5px; width: 344px; height: 275px;
    border: 1.2px dashed var(--dash); border-radius: 16px;
    text-align: center;
  }
  .dropzone svg { position: absolute; left: 142px; top: 38px; }
  .drop-title { position: absolute; left: 0; right: 0; top: 115px; font-size: 18px; font-weight: 700; }
  .drop-note { position: absolute; left: 20px; right: 20px; top: 146px; font-size: 12px; line-height: 21px; color: var(--ink-soft); }
  .btn-primary {
    position: absolute; left: 103px; top: 197px; width: 136px; height: 35px;
    background: var(--ink); color: #fff; border-radius: 18px;
    font-size: 12.5px; font-weight: 500;
    display: flex; align-items: center; justify-content: center;
  }

  .disclaimer { right: 25px; top: 572px; font-size: 13px; font-weight: 600; color: var(--accent); display: flex; align-items: center; gap: 6px; }

  /* Result rows */
  .row-card {
    left: 24px; width: 354px; height: 212px;
    background: var(--surface); border-radius: 20px;
  }
  .toolbar { position: absolute; top: 20px; display: flex; align-items: center; gap: 6px; font-size: 15px; font-weight: 500; }
  .toolbar.danger { color: var(--danger); }
  .tile {
    position: absolute; width: 100px; height: 132px; top: 59px;
    background: var(--surface); border-radius: 10px;
    box-shadow: 0 2px 8px rgba(15,27,52,0.08);
  }
  .tile-media {
    position: absolute; left: 2px; top: 5px; width: 96px; height: 95px; border-radius: 8px;
  }
  .tile-media.empty { background: var(--tile-empty); display: flex; align-items: center; justify-content: center; font-size: 8px; color: var(--ink-soft); }
  .tile-media.bw { background: linear-gradient(160deg, #8a8a86 0%, #3d3d3b 55%, #1e1e1d 100%); }
  .tile-media.vintage { background: linear-gradient(160deg, #6f8a6a 0%, #2e4f7a 45%, #1c2333 75%, #b98a66 100%); }
  .tile-media.real { background: linear-gradient(160deg, #7c8f6f 0%, #2c5285 45%, #1a2030 75%, #c79275 100%); }
  .badge {
    position: absolute; left: 4px; top: 4px; height: 12px; padding: 0 5px;
    background: var(--done); color: #fff; border-radius: 4px;
    font-size: 7px; font-weight: 600; display: flex; align-items: center; gap: 2px;
  }
  .badge::before { content: ""; width: 3px; height: 3px; border-radius: 50%; background: #fff; }
  .tile-label { position: absolute; left: 10px; top: 106px; font-size: 9.5px; font-weight: 600; }
  .tile-id { position: absolute; left: 10px; top: 104px; font-size: 8px; line-height: 10px; font-weight: 600; }
  .tile-dl { position: absolute; right: 8px; top: 105px; }
</style>
</head>
<body>
<main class="screen">

  <header>
    <div class="abs brand">huevista.ai</div>
    <div class="abs meter" style="left:212px"><div class="top">114 MB</div><div class="bottom">1.0 GB</div></div>
    <div class="abs meter" style="left:277px"><div class="top">4740</div><div class="bottom">credits</div></div>
    <div class="abs avatar">K</div>
  </header>

  <nav class="abs tabs">
    <span class="abs tab" style="left:40px">Images</span>
    <span class="abs tab" style="left:121px">Video Animations</span>
    <span class="abs tab" style="left:292px">Studio</span>
    <span class="abs tab-indicator"></span>
  </nav>

  <h2 class="abs section-title" style="top:163px">Upload Images</h2>
  <p class="abs section-copy" style="top:195px">Upload photos to generate vintage and real color versions.</p>

  <section class="abs upload">
    <div class="dropzone">
      <svg width="60" height="56" viewBox="0 0 60 56" fill="none" stroke="#0f1b34" stroke-width="4.5" stroke-linecap="round" stroke-linejoin="round">
        <path d="M30 33V4M18 15L30 4l12 11"/>
        <path d="M4 33v11a8 8 0 0 0 8 8h36a8 8 0 0 0 8-8V33"/>
      </svg>
      <div class="drop-title">Drag and drop images here</div>
      <div class="drop-note">Maximum 20 images 100MB total JPG, PNG, GIF, TIFF up to 10MB each</div>
      <div class="btn-primary">Select File</div>
    </div>
  </section>

  <h2 class="abs section-title" style="top:568px">Images</h2>
  <div class="abs disclaimer">
    <svg width="13" height="12" viewBox="0 0 13 12"><path d="M6.5 0.5L12.5 11.5H0.5Z" fill="#f5a524"/><rect x="5.9" y="4" width="1.2" height="4" fill="#fff"/><rect x="5.9" y="9" width="1.2" height="1.2" fill="#fff"/></svg>
    AI Disclaimer
  </div>
  <p class="abs section-copy" style="top:601px">Each row shows Original, Vintage Color, and Real Color.</p>

  <!-- Pending row -->
  <section class="abs row-card" style="top:669px">
    <div class="toolbar" style="left:32px">
      <svg width="15" height="15" viewBox="0 0 16 16" fill="none" stroke="#0f1b34" stroke-width="1.6" stroke-linecap="round"><path d="M3 8a5 5 0 1 0 1.6-3.7"/><path d="M3 2v3h3"/></svg>Rotate
    </div>
    <div class="toolbar danger" style="left:119px">
      <svg width="15" height="15" viewBox="0 0 16 16" fill="none" stroke="#e0383e" stroke-width="1.5" stroke-linecap="round"><path d="M2 4h12M6 4V2h4v2M3.5 4l1 10h7l1-10M6.5 7v4M9.5 7v4"/></svg>Delete
    </div>
    <div class="toolbar" style="left:203px">
      <svg width="17" height="14" viewBox="0 0 18 14" fill="none" stroke="#0f1b34" stroke-width="1.6" stroke-linecap="round" stroke-linejoin="round"><path d="M1 3h3c4 0 6 8 10 8h3M1 11h3c1.5 0 2.6-1 3.5-2.3M10.5 5.3C11.4 4 12.5 3 14 3h3M15 1l2 2-2 2M15 9l2 2-2 2"/></svg>Gernate (20)
    </div>

    <div class="tile" style="left:16px">
      <div class="tile-media bw" role="img" aria-label="Black and white family portrait, uploaded"></div>
      <div class="tile-id">Original ID:<br><span style="font-weight:500">0IO9YDY5</span></div>
      <svg class="tile-dl" width="11" height="11" viewBox="0 0 12 12" fill="none" stroke="#0f1b34" stroke-width="1.3" stroke-linecap="round"><path d="M6 1v6M3.5 4.5L6 7l2.5-2.5M1 8v3h10V8"/></svg>
    </div>
    <div class="tile" style="left:127px">
      <div class="tile-media empty">Not Gernated</div>
      <div class="tile-label">Vintage</div>
    </div>
    <div class="tile" style="left:239px">
      <div class="tile-media empty">Not Gernated</div>
      <div class="tile-label">Real</div>
    </div>
  </section>

  <!-- Completed row -->
  <section class="abs row-card" style="top:893px">
    <div class="toolbar" style="left:94px; top:23px; font-weight:500">Gernate time: 3m 2s</div>
    <div class="toolbar danger" style="left:264px; top:23px">
      <svg width="15" height="15" viewBox="0 0 16 16" fill="none" stroke="#e0383e" stroke-width="1.5" stroke-linecap="round"><path d="M2 4h12M6 4V2h4v2M3.5 4l1 10h7l1-10M6.5 7v4M9.5 7v4"/></svg>Delete
    </div>

    <div class="tile" style="left:16px">
      <div class="tile-media bw" role="img" aria-label="Black and white family portrait, uploaded"><span class="badge">Done</span></div>
      <div class="tile-id">Original ID:<br><span style="font-weight:500">0IO9YDY5</span></div>
      <svg class="tile-dl" width="11" height="11" viewBox="0 0 12 12" fill="none" stroke="#0f1b34" stroke-width="1.3" stroke-linecap="round"><path d="M6 1v6M3.5 4.5L6 7l2.5-2.5M1 8v3h10V8"/></svg>
    </div>
    <div class="tile" style="left:127px">
      <div class="tile-media vintage" role="img" aria-label="Family portrait in vintage color"><span class="badge">Done</span></div>
      <div class="tile-label">Vintage</div>
      <svg class="tile-dl" width="11" height="11" viewBox="0 0 12 12" fill="none" stroke="#0f1b34" stroke-width="1.3" stroke-linecap="round"><path d="M6 1v6M3.5 4.5L6 7l2.5-2.5M1 8v3h10V8"/></svg>
    </div>
    <div class="tile" style="left:239px">
      <div class="tile-media real" role="img" aria-label="Family portrait in real color"><span class="badge">Done</span></div>
      <div class="tile-label">Real</div>
      <svg class="tile-dl" width="11" height="11" viewBox="0 0 12 12" fill="none" stroke="#0f1b34" stroke-width="1.3" stroke-linecap="round"><path d="M6 1v6M3.5 4.5L6 7l2.5-2.5M1 8v3h10V8"/></svg>
    </div>
  </section>

</main>
</body>
</html>
```